依頼詳細
商品を販売したときに入れる手提袋のパッケージデザインを依頼します。現在の手提袋は紙製ですが、新しい手提袋はPP加工(マット加工)のもので、高級ブティックのような高級感あふれるものにしたいと思っています。
記載項目
【サイズ】
手提袋(小)
サイズ:W 180mm×H 189mm×幅 80mm
手提袋(大)
サイズ:W 240mm×H 250mm×幅 120mm

【記載項目】
・plain circle with 白羊
・屋号ロゴ
・代表商品(鶴のゼリー)名称
・HPのURL(http://www.kashi-hakuyo.example
・店舗情報
本店
白羊市 本町1丁目2-3 サンプルビル1F
TEL 000-555-0142
OPEN 11:00-20:00
不定休
あおば店
白羊市 若葉町4丁目5-6 テストビル2F
TEL011-520-2082
OPEN 月~土17:00-2:00 日17:00-24:00
不定休
希望イメージ
シンプル 複雑
単色 カラフル
暗い 明るい
日常 高級
遊び心 厳粛
未来的 伝統的
女性的 男性的
希望する色
黒、赤、白
納品ファイル
• 高解像度JPG (.jpg)
• イラストレーター形式 (.ai)
補足説明
黒バックに赤、白のようなデザインを考えていましたが、それ以外でもご提案頂ければと思います。
デザインで使用して頂きたいデータを追加します。
■ 選んだ理由

黒を基調としたシンプルなデザインでありながら、インパクトがある点を評価し選定させていただきました。

■ 提案者全員のお礼・コメント

ご連絡が遅くなり大変申し訳ございませんでした。
またたくさんのご応募を頂きまして有難うございました。
皆さまのご提案内容はそれぞれ大変素晴らしく絞るのが困難でした。

また機会がありましたらよろしくお願い致します。

```html
<!DOCTYPE html>
<html lang="ja">
<head>
<meta charset="UTF-8">
<title>鶴のゼリー 手提袋</title>
<link rel="stylesheet" href="https://fonts.googleapis.com/css2?family=Yuji+Syuku&family=Noto+Sans+JP:wght@400;700&display=swap">
<style>
  :root {
    --paper: #ffffff;
    --bag-dark: #2a1c18;
    --amber: #c8861f;
    --ink-light: #fdf6ea;
    --fold-line: #3a2820;
    --handle: #b9b9b9;
  }
  * { margin: 0; padding: 0; box-sizing: border-box; }
  html, body { width: 1200px; height: 1200px; overflow: hidden; background: var(--paper); }
  .canvas { position: relative; width: 1200px; height: 1200px; }
  .handles { position: absolute; left: 0; top: 0; }
  .bag-front { position: absolute; left: 32px; top: 330px; width: 788px; height: 824px; background: var(--bag-dark); }
  .front-band { position: absolute; left: 338px; top: 330px; width: 176px; height: 632px; background: var(--amber); }
  .hand-art {
    position: absolute; left: 318px; top: 330px; width: 498px; height: 370px;
    background: linear-gradient(90deg, rgba(224,176,114,0.22), rgba(224,176,114,0.08));
  }
  .product-name {
    position: absolute; left: 372px; top: 790px; width: 130px;
    font-family: "Yuji Syuku", serif; color: var(--ink-light);
    font-size: 42px; line-height: 1.15; white-space: nowrap;
    transform: rotate(-12deg); transform-origin: left top;
  }
  .product-name .line { display: block; }
  .product-name .line + .line { padding-left: 22px; }
  .product-name .particle { font-size: 22px; vertical-align: top; }
  .site-url {
    position: absolute; left: 66px; top: 894px;
    writing-mode: vertical-rl; transform: rotate(180deg);
    font-family: "Noto Sans JP", sans-serif; font-size: 8px; letter-spacing: .5px;
    color: var(--ink-light); opacity: .85; white-space: nowrap;
  }
  .front-mark { position: absolute; left: 58px; top: 1086px; display: flex; align-items: center; gap: 6px; }
  .front-mark .dot { width: 26px; height: 26px; border-radius: 50%; background: var(--ink-light); }
  .front-mark .name { font-family: "Noto Sans JP", sans-serif; font-size: 10px; font-weight: 700; color: var(--ink-light); }
  .bag-gusset { position: absolute; left: 820px; top: 330px; width: 350px; height: 824px; background: var(--bag-dark); }
  .gusset-panel { position: absolute; left: 840px; top: 330px; width: 310px; height: 824px; background: var(--amber); }
  .gusset-lines { position: absolute; left: 0; top: 0; }
  .shop-name {
    position: absolute; left: 866px; top: 696px; width: 114px; text-align: center;
    font-family: "Yuji Syuku", serif; color: var(--ink-light);
  }
  .shop-name .main { display: block; font-size: 44px; line-height: 1; }
  .shop-name .sub { display: block; font-family: "Noto Sans JP", sans-serif; font-weight: 700; font-size: 13px; margin-top: 6px; }
  .shop-name .latin { display: block; font-family: "Noto Sans JP", sans-serif; font-size: 6px; letter-spacing: 1px; margin-top: 3px; }
  .store-info {
    position: absolute; left: 890px; top: 822px; height: 200px;
    writing-mode: vertical-rl;
    font-family: "Noto Sans JP", sans-serif; font-size: 6.5px; line-height: 2;
    color: var(--ink-light);
  }
  .store-info .branch { margin-left: 8px; }
</style>
</head>
<body>
<div class="canvas">
  <svg class="handles" width="1200" height="340" viewBox="0 0 1200 340" aria-hidden="true">
    <path d="M176 332 C190 150 300 46 425 46 C550 46 660 150 674 332" fill="none" stroke="var(--handle)" stroke-width="2"/>
    <path d="M188 332 C202 162 308 58 425 58 C542 58 648 162 662 332" fill="none" stroke="var(--handle)" stroke-width="2"/>
  </svg>

  <div class="bag-front"></div>
  <div class="front-band"></div>
  <div class="hand-art" role="img" aria-label="手の線画イラスト"></div>
  <div class="product-name">
    <span class="line">鶴<span class="particle">の</span></span>
    <span class="line">ゼリー</span>
  </div>
  <div class="site-url">http://www.kashi-hakuyo.example</div>
  <div class="front-mark"><span class="dot"></span><span class="name">白羊</span></div>

  <div class="bag-gusset"></div>
  <div class="gusset-panel"></div>
  <svg class="gusset-lines" width="1200" height="1200" viewBox="0 0 1200 1200" aria-hidden="true">
    <line x1="996" y1="330" x2="996" y2="1008" stroke="var(--fold-line)" stroke-width="1"/>
    <line x1="996" y1="1008" x2="840" y2="1154" stroke="var(--fold-line)" stroke-width="1"/>
    <line x1="996" y1="1008" x2="1150" y2="1154" stroke="var(--fold-line)" stroke-width="1"/>
  </svg>

  <div class="shop-name">
    <span class="main">白羊</span>
    <span class="sub">菓子</span>
    <span class="latin">KASHI HAKUYO</span>
  </div>

  <div class="store-info">
    <p>本店</p>
    <p>白羊市 本町1丁目2-3 サンプルビル1F</p>
    <p>TEL 000-555-0142</p>
    <p>OPEN 11:00-20:00 不定休</p>
    <p class="branch">あおば店</p>
    <p>白羊市 若葉町4丁目5-6 テストビル2F</p>
    <p>TEL 000-555-0187</p>
    <p>OPEN 月~土17:00-2:00 日17:00-24:00 不定休</p>
  </div>
</div>
</body>
</html>
```